Post Lockdown Ortho Special

We are running a special for (Ortho) Braces/Clear Aligner (Quorventa), till July 31st 2020. Up to $2,000 off with free Consultation and Xrays.

We need a ad to run in different formats.

Maybe something with: what better time to get braces when you have to wear a mask all the time.

Trying to rebuild our business and get people in for free consultations.

```html
<!DOCTYPE html>
<html lang="en">
<head>
<meta charset="utf-8">
<title>Post Lockdown Ortho Special – Ad Formats</title>
<link href="https://fonts.googleapis.com/css2?family=Oswald:wght@500;700&family=Open+Sans:wght@400;600;700&display=swap" rel="stylesheet">
<style>
  :root {
    --purple: #5a2d86;
    --purple-dark: #45206a;
    --navy: #1d4b7c;
    --white: #ffffff;
    --ink: #3a3a3a;
    --label: #d7e2ee;
    --photo-a: #eceae8;
    --photo-b: #cfc7c2;
    --teeth-a: #f2b7bd;
    --teeth-b: #e9ecef;
  }
  * { box-sizing: border-box; margin: 0; padding: 0; }
  html, body { width: 849px; height: 1200px; overflow: hidden; background: var(--white); }
  .sheet { position: relative; width: 849px; height: 1200px; background: var(--navy); overflow: hidden; font-family: "Open Sans", sans-serif; }

  .ad { position: absolute; background: var(--white); overflow: hidden; color: var(--purple); }
  .ad-text { position: absolute; left: 0.7em; top: 0.55em; width: 58%; z-index: 2; }
  .brand { display: flex; align-items: center; gap: 0.3em; font-family: "Open Sans", sans-serif; font-weight: 700; font-size: 0.5em; letter-spacing: 0.12em; text-transform: uppercase; color: var(--purple); }
  .brand-mark { width: 1.3em; height: 1.3em; background: var(--purple); }
  .title { font-family: "Oswald", sans-serif; font-weight: 700; font-size: 2.6em; line-height: 1; margin-top: 0.12em; letter-spacing: 0.01em; white-space: nowrap; }
  .sub { font-size: 0.52em; color: var(--ink); margin-top: 0.15em; white-space: nowrap; }
  .deal { display: inline-block; background: var(--purple-dark); color: var(--white); font-weight: 600; font-size: 0.5em; padding: 0.35em 2.2em 0.35em 0.6em; margin-top: 0.5em; white-space: nowrap; }
  .free { font-family: "Oswald", sans-serif; font-weight: 500; font-size: 0.85em; text-transform: uppercase; margin-top: 0.35em; white-space: nowrap; }
  .copy { font-size: 0.44em; color: var(--ink); line-height: 1.35; margin-top: 0.3em; width: 70%; }

  .photo { position: absolute; right: 0; top: 0; bottom: 0; width: 38%; background: radial-gradient(ellipse at 50% 40%, var(--photo-a), var(--photo-b)); }
  .teeth { position: absolute; left: 40%; bottom: 10%; width: 15%; height: 24%; border-radius: 40% 40% 30% 30%; background: linear-gradient(180deg, var(--teeth-b), var(--teeth-a)); z-index: 1; }

  .hero { left: 0; top: 0; width: 849px; height: 335px; font-size: 24px; }
  .hero .ad-text { left: 22px; top: 10px; }
  .hero .copy { width: 45%; }
  .hero .photo { width: 40%; }
  .hero .teeth { left: 37%; bottom: 14%; width: 15%; height: 20%; }

  .universal .ad-text { width: 90%; }
  .universal .photo { top: 48%; width: 45%; }
  .universal .teeth { left: 8%; bottom: 6%; width: 30%; height: 22%; }
  .universal .copy { width: 48%; }

  .format-label { position: absolute; font-size: 6.5px; color: var(--label); white-space: nowrap; }
</style>
</head>
<body>
<div class="sheet">

  <section class="ad hero">
    <div class="ad-text">
      <div class="brand"><span class="brand-mark"></span>Larkmoor</div>
      <h1 class="title">SPECIAL OFFER</h1>
      <p class="sub">(Ortho) Braces/Clear Aligner (Quorventa)</p>
      <p class="deal">Till July 31st 2020. Up To $2,000 OFF</p>
      <p class="free">Free Consultation and Xrays</p>
      <p class="copy">what better time to get braces when you have to wear a mask all the time.</p>
    </div>
    <div class="teeth" role="img" aria-label="Dental model of teeth with braces"></div>
    <div class="photo" role="img" aria-label="Photo of a woman wearing a face mask"></div>
  </section>

  <p class="format-label" style="left:28px;top:348px">Network Profile Banner (1584 x 396 px)</p>

  <p class="format-label" style="left:76px;top:412px">Blog Banner (3000 x 1055 px)</p>
  <section class="ad" style="left:76px;top:424px;width:326px;height:136px;font-size:8.5px">
    <div class="ad-text">
      <div class="brand"><span class="brand-mark"></span>Larkmoor</div>
      <h2 class="title">SPECIAL OFFER</h2>
      <p class="sub">(Ortho) Braces/Clear Aligner (Quorventa)</p>
      <p class="deal">Till July 31st 2020. Up To $2,000 OFF</p>
      <p class="free">Free Consultation and Xrays</p>
      <p class="copy">what better time to get braces when you have to wear a mask all the time.</p>
    </div>
    <div class="teeth" role="img" aria-label="Dental model of teeth with braces"></div>
    <div class="photo" role="img" aria-label="Photo of a woman wearing a face mask"></div>
  </section>

  <p class="format-label" style="left:504px;top:412px">Circle Cover (1080 x 608 px)</p>
  <section class="ad" style="left:504px;top:424px;width:277px;height:142px;font-size:8px">
    <div class="ad-text">
      <div class="brand"><span class="brand-mark"></span>Larkmoor</div>
      <h2 class="title">SPECIAL OFFER</h2>
      <p class="sub">(Ortho) Braces/Clear Aligner (Quorventa)</p>
      <p class="deal">Till July 31st 2020. Up To $2,000 OFF</p>
      <p class="free">Free Consultation and Xrays</p>
      <p class="copy">what better time to get braces when you have to wear a mask all the time.</p>
    </div>
    <div class="teeth" role="img" aria-label="Dental model of teeth with braces"></div>
    <div class="photo" role="img" aria-label="Photo of a woman wearing a face mask"></div>
  </section>

  <p class="format-label" style="left:76px;top:604px">Feed Event Cover (1920 x 1080 px)</p>
  <section class="ad" style="left:76px;top:617px;width:295px;height:124px;font-size:7.6px">
    <div class="ad-text">
      <div class="brand"><span class="brand-mark"></span>Larkmoor</div>
      <h2 class="title">SPECIAL OFFER</h2>
      <p class="sub">(Ortho) Braces/Clear Aligner (Quorventa)</p>
      <p class="deal">Till July 31st 2020. Up To $2,000 OFF</p>
      <p class="free">Free Consultation and Xrays</p>
      <p class="copy">what better time to get braces when you have to wear a mask all the time.</p>
    </div>
    <div class="teeth" role="img" aria-label="Dental model of teeth with braces"></div>
    <div class="photo" role="img" aria-label="Photo of a woman wearing a face mask"></div>
  </section>

  <p class="format-label" style="left:402px;top:596px">Social Media Universal Post (1200 x 1200 px)</p>
  <section class="ad universal" style="left:402px;top:608px;width:362px;height:360px;font-size:15px">
    <div class="ad-text">
      <div class="brand"><span class="brand-mark"></span>Larkmoor</div>
      <h2 class="title">SPECIAL OFFER</h2>
      <p class="sub">(Ortho) Braces/Clear Aligner (Quorventa)</p>
      <p class="deal">Till July 31st 2020. Up To $2,000 OFF</p>
      <p class="free">Free Consultation and Xrays</p>
      <p class="copy">what better time to get braces when you have to wear a mask all the time.</p>
    </div>
    <div class="teeth" role="img" aria-label="Dental model of teeth with braces"></div>
    <div class="photo" role="img" aria-label="Photo of a woman wearing a face mask"></div>
  </section>

  <p class="format-label" style="left:76px;top:746px">Feed Ad (1200 x 628 px)</p>
  <section class="ad" style="left:76px;top:758px;width:300px;height:162px;font-size:9px">
    <div class="ad-text">
      <div class="brand"><span class="brand-mark"></span>Larkmoor</div>
      <h2 class="title">SPECIAL OFFER</h2>
      <p class="sub">(Ortho) Braces/Clear Aligner (Quorventa)</p>
      <p class="deal">Till July 31st 2020. Up To $2,000 OFF</p>
      <p class="free">Free Consultation and Xrays</p>
      <p class="copy">what better time to get braces when you have to wear a mask all the time.</p>
    </div>
    <div class="teeth" role="img" aria-label="Dental model of teeth with braces"></div>
    <div class="photo" role="img" aria-label="Photo of a woman wearing a face mask"></div>
  </section>

  <p class="format-label" style="left:76px;top:967px">Stream Image App Card (800 x 320 px)</p>
  <section class="ad" style="left:76px;top:979px;width:196px;height:74px;font-size:5px">
    <div class="ad-text">
      <div class="brand"><span class="brand-mark"></span>Larkmoor</div>
      <h2 class="title">SPECIAL OFFER</h2>
      <p class="sub">(Ortho) Braces/Clear Aligner (Quorventa)</p>
      <p class="deal">Till July 31st 2020. Up To $2,000 OFF</p>
      <p class="free">Free Consultation and Xrays</p>
      <p class="copy">what better time to get braces when you have to wear a mask all the time.</p>
    </div>
    <div class="teeth" role="img" aria-label="Dental model of teeth with braces"></div>
    <div class="photo" role="img" aria-label="Photo of a woman wearing a face mask"></div>
  </section>

  <p class="format-label" style="left:402px;top:1000px">Stream Header (1500 x 500 px)</p>
  <section class="ad" style="left:402px;top:1013px;width:320px;height:111px;font-size:7.2px">
    <div class="ad-text">
      <div class="brand"><span class="brand-mark"></span>Larkmoor</div>
      <h2 class="title">SPECIAL OFFER</h2>
      <p class="sub">(Ortho) Braces/Clear Aligner (Quorventa)</p>
      <p class="deal">Till July 31st 2020. Up To $2,000 OFF</p>
      <p class="free">Free Consultation and Xrays</p>
      <p class="copy">what better time to get braces when you have to wear a mask all the time.</p>
    </div>
    <div class="teeth" role="img" aria-label="Dental model of teeth with braces"></div>
    <div class="photo" role="img" aria-label="Photo of a woman wearing a face mask"></div>
  </section>

</div>
</body>
</html>
```